Custom hot rod builder needs a website for launch of new business where he will build luxury garages

We need a website that gives a WOW first impression for "Summit Carhouses". This is a new business so photos are renderings but we need it to really attract a particular audience. Our initial business is custom hot rods so now we are building garages for them. These will be like luxury "homes" for cars! I will attach our new logo. Website needs to feel powerful and prestigious.

Target Market(s)

middle aged men, car enthusiasts

Industry/Entity Type

automotive, construction

Coding

Coded - Design and coding required

Number of Pages Required

2 page

Font styles to use
Serif

Colors
0054AA
0677BA
7BADD7
CADEEF
E8F1F8

Requirements
Must have
• a WOW factor. luxury. contact form.
Nice to have
• ?

```html
<!DOCTYPE html>
<html lang="en">
<head>
<meta charset="utf-8">
<title>Summit Carhouses</title>
<link href="https://fonts.googleapis.com/css2?family=Michroma&family=Mulish:wght@400;600;700&family=Oswald:wght@500&display=swap" rel="stylesheet">
<style>
:root{
  --black:#000;
  --royal:#0054aa;
  --ocean:#0677ba;
  --sky:#29a8e0;
  --mist:#cadeef;
  --ice:#e8f1f8;
  --white:#fff;
  --ink:#333;
  --muted:#555;
  --grey-card:#d4d4d6;
}
*{margin:0;padding:0;box-sizing:border-box}
html,body{width:1200px;height:3995px;overflow:hidden;background:var(--black)}
body{font-family:'Mulish',sans-serif;color:var(--white);position:relative}
.abs{position:absolute}
.display{font-family:'Michroma',sans-serif;font-variant:small-caps;letter-spacing:4px;text-transform:lowercase}
.btn{position:absolute;display:flex;align-items:center;justify-content:center;background:var(--sky);color:var(--white);font-size:16px;border-radius:3px}
.underline{position:absolute;height:4px;border-radius:50%;background:var(--ocean)}

/* header */
.site-header{position:absolute;left:0;top:0;width:1200px;height:90px;background:var(--black)}
.brand{position:absolute;left:186px;top:22px;display:flex;align-items:center;gap:12px;font-weight:700;font-size:24px;color:var(--sky)}
.brand .dot{width:40px;height:40px;border-radius:50%;background:var(--sky)}
.nav{position:absolute;top:32px;font-size:14px;color:var(--white)}
.nav.active{color:var(--sky);border-bottom:2px solid var(--sky);padding-bottom:4px}
.nav-phone{position:absolute;left:855px;top:28px;font-size:20px;color:var(--ocean);display:flex;align-items:center;gap:8px}
.nav-divider{position:absolute;left:838px;top:18px;width:1px;height:46px;background:#555}

/* hero */
.hero{position:absolute;left:0;top:90px;width:1200px;height:560px;overflow:hidden}
.hero-img{position:absolute;inset:0;background:linear-gradient(180deg,#3b2a1c 0%,#6b4a2c 35%,#4a6b5a 60%,#7a4a30 100%)}
.hero h1{position:absolute;left:0;width:1200px;top:122px;text-align:center;font-family:'Oswald',sans-serif;font-weight:500;font-size:40px;color:var(--white)}
.arrow{position:absolute;top:258px;width:36px;height:36px;border:1.5px solid var(--white);border-radius:50%}

/* welcome */
.welcome-img{left:186px;top:724px;width:334px;height:296px;background:linear-gradient(180deg,#9fb0be 0%,#d8d8d4 50%,#7e8a7c 100%)}
.badge{left:340px;top:887px;width:192px;height:155px;background:#5c646a;border:3px solid #ddd;color:var(--white)}
.badge .num{position:absolute;left:22px;top:6px;font-family:'Oswald',sans-serif;font-size:100px;line-height:1}
.badge .plus{position:absolute;left:148px;top:80px;font-size:28px}
.badge .sub{position:absolute;left:24px;top:116px;font-size:20px}
.welcome h2{position:absolute;left:567px;top:710px;font-size:29px;line-height:32px}
.body-text{font-size:12.5px;line-height:23px;color:#ccc}

/* offer */
.section-title{position:absolute;left:0;width:1200px;text-align:center;font-size:29px}
.blue{color:var(--royal)}
.light{color:var(--sky)}
.offer-card{position:absolute;width:404px;height:112px;background:var(--white);color:var(--ink)}
.offer-card .ic{position:absolute;left:22px;top:30px;width:54px;height:54px;border-radius:50%;background:var(--white);box-shadow:0 2px 8px rgba(0,0,0,.15);display:flex;align-items:center;justify-content:center}
.offer-card h3{position:absolute;left:94px;top:26px;font-size:14px;color:var(--royal);font-weight:600}
.offer-card p{position:absolute;left:94px;top:48px;width:292px;font-size:11px;line-height:20px;color:#444}

/* cta */
.cta-blue{left:192px;top:1530px;width:813px;height:252px;background:var(--royal);border-radius:10px;box-shadow:0 18px 20px -10px #0a2a55}
.cta-title{position:absolute;left:0;width:100%;text-align:center;font-size:30px;line-height:40px}

/* gallery */
.tile{position:absolute;width:262px;height:262px;background:var(--ice)}
.tile .photo{position:absolute;left:0;top:0;width:262px;height:222px}
.tile .cap{position:absolute;left:0;top:222px;width:262px;height:40px;display:flex;align-items:center;justify-content:center;font-size:12.5px;color:#333;background:#e4e4e4}
.tile.active{box-shadow:0 0 14px #2a5ca8}
.tile.active .cap{background:var(--royal);color:var(--white)}

/* reviews */
.review{position:absolute;width:396px;height:196px;background:var(--grey-card);border-radius:4px;color:#333;box-shadow:0 0 10px rgba(255,255,255,.3)}
.review p{position:absolute;left:26px;top:22px;width:346px;font-size:11px;line-height:20px}
.review .who{position:absolute;left:24px;top:130px;font-size:13px;color:var(--royal);font-weight:600}
.review .stars{position:absolute;left:24px;top:152px;font-size:14px;color:#f5a623;letter-spacing:1px}
.review .quote{position:absolute;right:22px;top:104px;font-size:110px;line-height:1;color:#aeb0b4;font-family:Georgia,serif}
.dash{position:absolute;top:2957px;width:24px;height:3px;background:var(--white)}

/* footer */
.footer{position:absolute;left:0;top:3380px;width:1200px;height:570px}
.footer-brand{position:absolute;left:192px;top:92px;display:flex;align-items:center;gap:10px;font-weight:700;font-size:24px;color:#6f95c9}
.footer-brand .dot{width:40px;height:40px;border-radius:50%;background:#6f95c9}
.f-title{position:absolute;font-size:15px;letter-spacing:3px}
.f-item{position:absolute;font-size:12.5px;line-height:19px;color:var(--white)}
.field{position:absolute;height:36px;border-bottom:1px solid #4f7fc0;font-size:11.5px;color:var(--white);display:flex;align-items:flex-start;gap:10px}
.copyright{position:absolute;left:0;top:3950px;width:1200px;height:45px;background:#111;display:flex;align-items:center;justify-content:center;font-size:12px;color:var(--white)}
</style>
</head>
<body>

<header class="site-header">
  <div class="brand"><span class="dot"></span>Summit Carhouses</div>
  <span class="nav active" style="left:575px">Home</span>
  <span class="nav" style="left:639px">Work Gallery</span>
  <span class="nav" style="left:751px">Contact Us</span>
  <span class="nav-divider"></span>
  <span class="nav-phone">
    <svg width="20" height="20" viewBox="0 0 24 24" fill="none" stroke="currentColor" stroke-width="1.6"><path d="M5 3h4l2 5-3 2a11 11 0 0 0 6 6l2-3 5 2v4a2 2 0 0 1-2 2A18 18 0 0 1 3 5a2 2 0 0 1 2-2z"/></svg>
    123.456.7890
  </span>
</header>

<section class="hero">
  <div class="hero-img" role="img" aria-label="Rendering of a luxury garage interior with hot rods and classic cars on a wooden floor"></div>
  <h1>We Build Custom Hot Rod Luxury Garages</h1>
  <a class="btn" style="left:526px;top:176px;width:148px;height:42px">Contact Us Today</a>
  <span class="arrow" style="left:90px"></span>
  <span class="arrow" style="left:1078px"></span>
  <svg class="abs" style="left:0;top:440px" width="1200" height="120" viewBox="0 0 1200 120" preserveAspectRatio="none">
    <path d="M0 62 C200 30 330 40 420 55 C560 80 700 30 900 70 C1020 90 1120 100 1200 90 L1200 120 L0 120 Z" fill="#0677ba"/>
    <path d="M0 85 C220 45 330 52 430 66 C560 90 700 50 900 88 C1020 106 1120 112 1200 104 L1200 120 L0 120 Z" fill="#000"/>
  </svg>
</section>

<section class="welcome">
  <div class="abs welcome-img" role="img" aria-label="Rendering of a modern luxury carhouse with palm trees"></div>
  <div class="abs badge"><span class="num">20</span><span class="plus">+</span><span class="sub">Years Experience</span></div>
  <h2 class="display"><span class="light">Welcome To</span><br><span class="light">Summit</span> <span class="blue">Carhouses</span></h2>
  <span class="underline" style="left:567px;top:795px;width:56px"></span>
  <p class="abs body-text" style="left:567px;top:810px;width:446px">Lorem ipsum dolor sit amet, consectetuer adipiscing elit, sed dim nonummy nibh euismod tincidunt ut laoreet dolore magna aliquam erat volutpat. Ut wisi enim ad minim veniam, quis nostrud exerci.</p>
  <p class="abs body-text" style="left:567px;top:886px;width:446px">Lorem ipsum dolor sit amet, consectetuer adipiscing elit, sed dim nonummy nibh euismod tincidunt ut laoreet dolore magna aliquam erat volutpat. Ut wisi enim ad minim veniam, quis nostrud exerci tation ullamcorper suscipit lobortis nisl ut aliquip ex ea commodo consequat. Duis aute</p>
  <a class="btn" style="left:566px;top:987px;width:128px;height:42px">Contact Us</a>
</section>

<section class="offer">
  <h2 class="section-title display" style="top:1132px"><span class="light">What</span> <span class="blue">We</span> <span class="light">Offer</span></h2>
  <span class="underline" style="left:572px;top:1173px;width:56px"></span>

  <div class="offer-card" style="left:186px;top:1210px">
    <span class="ic"><svg width="30" height="30" viewBox="0 0 30 30" fill="none" stroke="#333" stroke-width="1.4"><path d="M3 12l6-4 6 3 6-3 6 4M8 14l5 5 3-2 3 2 4-4"/></svg></span>
    <h3>Loyalty Programs</h3>
    <p>Lorem ipsum dolor sit amet, consectetuer adipiscing elit, sed dim nonummy nibh euismod.</p>
  </div>
  <div class="offer-card" style="left:608px;top:1210px">
    <span class="ic"><svg width="30" height="30" viewBox="0 0 30 30" fill="none" stroke="#333" stroke-width="1.4"><circle cx="15" cy="12" r="8"/><path d="M15 8l1.3 2.7 3 .4-2.2 2 .6 3-2.7-1.5-2.7 1.5.6-3-2.2-2 3-.4zM10 19l-2 8 7-3 7 3-2-8"/></svg></span>
    <h3>20 Years Experience</h3>
    <p>Lorem ipsum dolor sit amet, consectetuer adipiscing elit, sed dim nonummy nibh euismod.</p>
  </div>
  <div class="offer-card" style="left:186px;top:1344px">
    <span class="ic"><svg width="30" height="30" viewBox="0 0 30 30" fill="none" stroke="#333" stroke-width="1.4"><path d="M16 4h10v10L14 26 4 16z"/><circle cx="21" cy="9" r="1.5"/></svg></span>
    <h3>Always The Best Value</h3>
    <p>Lorem ipsum dolor sit amet, consectetuer adipiscing elit, sed dim nonummy nibh euismod.</p>
  </div>
  <div class="offer-card" style="left:608px;top:1344px">
    <span class="ic"><svg width="30" height="30" viewBox="0 0 30 30" fill="none" stroke="#333" stroke-width="1.4"><path d="M7 15v-2a8 8 0 0 1 16 0v2"/><rect x="5" y="14" width="4" height="6" rx="1"/><rect x="21" y="14" width="4" height="6" rx="1"/><path d="M8 27c1-4 4-5 7-5s6 1 7 5"/></svg></span>
    <h3>24 Hour Customer Service Available</h3>
    <p>Lorem ipsum dolor sit amet, consectetuer adipiscing elit, sed dim nonummy nibh euismod.</p>
  </div>
</section>

<section class="abs cta-blue">
  <h2 class="cta-title display" style="top:60px">To Build Your<br>Luxury “Homes” For Cars!</h2>
  <a class="btn" style="left:332px;top:146px;width:148px;height:40px">Contact Us Today</a>
</section>

<section class="gallery">
  <h2 class="section-title display" style="top:1874px"><span class="light">Work</span> <span class="blue">Gallery</span></h2>
  <span class="underline" style="left:572px;top:1915px;width:56px"></span>

  <div class="tile active" style="left:186px;top:1943px"><div class="photo" role="img" aria-label="Two hot rods parked in a bright showroom" style="background:linear-gradient(135deg,#4a3a2a,#8a3030 60%,#cfd6e0)"></div><span class="cap">Project 1 @ Harbor Row, Eastfield</span></div>
  <div class="tile" style="left:468px;top:1943px"><div class="photo" role="img" aria-label="Luxury garage interior with classic cars" style="background:linear-gradient(180deg,#4a2e1c,#7a5a3a 55%,#3e5a4a)"></div><span class="cap">Project 2 @ Harbor Row, Eastfield</span></div>
  <div class="tile" style="left:752px;top:1943px"><div class="photo" role="img" aria-label="Hot rod workshop with cars under construction" style="background:linear-gradient(180deg,#3a3530,#6a6258 60%,#4a4a48)"></div><span class="cap">Project 3 @ Harbor Row, Eastfield</span></div>
  <div class="tile" style="left:186px;top:2236px"><div class="photo" role="img" aria-label="Vintage dark blue roadster in a museum hall" style="background:linear-gradient(180deg,#8a7a6a,#2a3050 55%,#d8d8d8)"></div><span class="cap">Project 4 @ Harbor Row, Eastfield</span></div>
  <div class="tile" style="left:468px;top:2236px"><div class="photo" role="img" aria-label="Yellow and black hot rods on a dark showroom floor" style="background:linear-gradient(180deg,#1a1a1a,#7a6a20 55%,#222)"></div><span class="cap">Project 5 @ Harbor Row, Eastfield</span></div>
  <div class="tile" style="left:752px;top:2236px"><div class="photo" role="img" aria-label="Rat rod in a large workshop bay" style="background:linear-gradient(180deg,#4a4038,#5a3a3a 55%,#6a6660)"></div><span class="cap">Project 6 @ Harbor Row, Eastfield</span></div>

  <a class="btn" style="left:527px;top:2535px;width:127px;height:41px">View All</a>
</section>

<section class="reviews">
  <h2 class="section-title display" style="top:2652px"><span class="light">Happy</span> <span class="blue">Customer</span> <span class="light">Reviews</span></h2>
  <span class="underline" style="left:572px;top:2693px;width:56px"></span>

  <div class="review" style="left:190px;top:2726px">
    <p>Lorem ipsum dolor sit amet, consectetuer adipiscing elit, sed dim nonummy nibh euismod tincidunt ut laoreet dore magna aliquam erat volutpat. Ut wisi enim ad minim veniam, quis nostrud exerci tation ullamcorper suscipit lobortis nisl ut aliquip ex ea commodo consequat. Duis aute</p>
    <span class="who">Marla T.</span><span class="stars">★★★★★</span><span class="quote">”</span>
  </div>
  <div class="review" style="left:617px;top:2726px">
    <p>Lorem ipsum dolor sit amet, consectetuer adipiscing elit, sed dim nonummy nibh euismod tincidunt ut laoreet dore magna aliquam erat volutpat. Ut wisi enim ad minim veniam, quis nostrud exerci tation ullamcorper suscipit lobortis nisl ut aliquip ex ea commodo consequat. Duis aute</p>
    <span class="who">Denise R.</span><span class="stars">★★★★★</span><span class="quote">”</span>
  </div>
  <span class="dash" style="left:520px"></span>
  <span class="dash" style="left:554px"></span>
  <span class="dash" style="left:588px;background:var(--ocean)"></span>
  <span class="dash" style="left:622px"></span>
  <span class="dash" style="left:656px"></span>
</section>

<section class="abs" style="left:222px;top:3260px;width:756px;height:28px;background:#2a2a2a;border-radius:0 0 10px 10px"></section>
<section class="abs" style="left:194px;top:3032px;width:812px;height:250px;background:var(--white);border-radius:10px">
  <h2 class="cta-title display blue" style="top:64px">To Build Your<br>Luxury custom hot rods Garages!</h2>
  <a class="btn" style="left:332px;top:146px;width:148px;height:40px">Contact Us Today</a>
</section>

<footer class="footer">
  <svg class="abs" style="left:0;top:0" width="1200" height="570" viewBox="0 0 1200 570" preserveAspectRatio="none">
    <path d="M0 50 C200 -10 420 10 620 40 C820 70 1000 70 1200 20 L1200 570 L0 570 Z" fill="#0054aa"/>
    <path d="M380 5 C600 10 800 60 980 55 C1080 52 1150 40 1200 20 L1200 40 C1140 60 1060 78 960 76 C780 72 600 20 380 5 Z" fill="#29a8e0"/>
  </svg>
  <div class="footer-brand"><span class="dot"></span>Summit Carhouses</div>

  <h3 class="f-title display" style="left:191px;top:176px"><span class="light">Contact</span> Details</h3>
  <span class="underline" style="left:191px;top:200px;width:52px;background:var(--white)"></span>
  <svg class="abs" style="left:188px;top:222px" width="20" height="24" viewBox="0 0 20 24" fill="none" stroke="#7badd7" stroke-width="1.4"><path d="M10 23s7-8 7-13a7 7 0 0 0-14 0c0 5 7 13 7 13z"/><circle cx="10" cy="10" r="2.5"/></svg>
  <p class="f-item" style="left:222px;top:222px">Summit Carhouses<br>Street Name, City Name<br>State Zipcode</p>
  <svg class="abs" style="left:188px;top:308px" width="22" height="22" viewBox="0 0 24 24" fill="none" stroke="#7badd7" stroke-width="1.4"><path d="M5 3h4l2 5-3 2a11 11 0 0 0 6 6l2-3 5 2v4a2 2 0 0 1-2 2A18 18 0 0 1 3 5a2 2 0 0 1 2-2z"/></svg>
  <p class="f-item" style="left:222px;top:307px">Call Us<br>123.456.7890</p>
  <svg class="abs" style="left:188px;top:374px" width="22" height="20" viewBox="0 0 22 20" fill="none" stroke="#7badd7" stroke-width="1.4"><rect x="1" y="5" width="20" height="14"/><path d="M1 5l10 8 10-8"/></svg>
  <p class="f-item" style="left:222px;top:372px">Email Us<br>hello@summitcarhouses.com</p>
  <svg class="abs" style="left:188px;top:436px" width="20" height="24" viewBox="0 0 20 24" fill="none" stroke="#7badd7" stroke-width="1.4"><path d="M10 23s7-8 7-13a7 7 0 0 0-14 0c0 5 7 13 7 13z"/><circle cx="10" cy="10" r="2.5"/></svg>
  <p class="f-item" style="left:222px;top:435px">Location Map<br><span style="color:#7badd7;text-decoration:underline">View Directions</span></p>

  <h3 class="f-title display" style="left:508px;top:176px"><span class="light">Get</span> In Touch</h3>
  <span class="underline" style="left:508px;top:200px;width:52px;background:var(--white)"></span>
  <p class="f-item" style="left:505px;top:212px;font-size:11px;line-height:18px">If you would like to know more about our services please call or provide the information below.<br>Thank you for your interest in Summit Carhouses</p>
  <div class="field" style="left:506px;top:258px;width:238px"><span style="color:#7badd7">◯</span>First Name</div>
  <div class="field" style="left:774px;top:258px;width:240px"><span style="color:#7badd7">◯</span>Last Name</div>
  <div class="field" style="left:506px;top:312px;width:238px"><span style="color:#7badd7">✉</span>Email</div>
  <div class="field" style="left:774px;top:306px;width:240px"><span style="color:#7badd7">☏</span>Phone</div>
  <div class="field" style="left:506px;top:360px;width:508px;height:64px"><span style="color:#7badd7">▭</span>Message</div>
  <a class="btn" style="left:504px;top:446px;width:148px;height:42px">Submit Now</a>
</footer>

<div class="copyright">© 2022 Summit Carhouses. All Rights Reserved.</div>

</body>
</html>
```